A Freight forwarding (transportation/shipping) company requires stationary design

We need The following:
1. Letterhead
2. Letter Envelope
3. A4 Paper Envelope
4. A4 Paper Folder (One that is 2xA4 foldable size which we can open in half and we can put a paper in between)
5. A5 Paper (To be used for notes taking)

a design for a freight forwarding company named BORUMAND TALAJ INTERNATIONAL TRANSPORTATION CO . Business Card is already designed and should follow it, the files attached help guide you in type of docs required + Logos (We are active in Sea Transportation, Truck transportation, and Air Transportation, (printed design is required with all open source files for editing - lamination accepted)

The said company is agent and sales representative of 2 other Shipping companies (whose logos, name, and website should also be mentioned on Envelopes and Folder) - Velor Tide and QMD Shipping, logos attached.

Velor Tide Shipping LLC
Dubai, United Arab Emirates
www.vtduae-example.com

QMD Shipping Line Ltd
London, United Kingdom
www.qmdfleet-example.com

Address is "No.8, 2nd Sadaf Kuy-e-Nilufari, Tehran, IR
Tel number is +98 21 55402913
Fax number is +98 21 55406287
E-Mail address is info@borumandtalaj-example.com
Website is www.borumandtalaj-example.com

```html
<!DOCTYPE html>
<html lang="en">
<head>
<meta charset="utf-8">
<title>Borumand Talaj Stationery</title>
<link href="https://fonts.googleapis.com/css2?family=Poppins:ital,wght@0,400;0,500;0,600;1,500&display=swap" rel="stylesheet">
<style>
  :root {
    --backdrop: #c8c8c8;
    --paper: #ffffff;
    --navy: #0a3550;
    --flap: #174f6c;
    --flap-mark: #124660;
    --brand-blue: #2f6fb5;
    --ink: #1a1a1a;
    --faint: #efefef;
  }
  html, body {
    margin: 0;
    padding: 0;
    width: 1200px;
    height: 1200px;
    overflow: hidden;
    background: var(--backdrop);
    font-family: "Poppins", sans-serif;
  }
  .canvas { position: relative; width: 1200px; height: 1200px; }

  .envelope {
    position: absolute;
    left: 132px; top: 357px;
    width: 404px; height: 571px;
    background: var(--paper);
    box-shadow: 0 1px 3px rgba(0,0,0,0.18);
    overflow: hidden;
  }
  .envelope__flap { position: absolute; left: 0; top: 0; }
  .envelope__watermark { position: absolute; left: 110px; top: 221px; }
  .envelope__rule {
    position: absolute; left: 0; right: 0; top: 538px;
    height: 3px; background: var(--navy);
  }
  .envelope__band {
    position: absolute; left: 0; right: 0; bottom: 0;
    height: 26px; background: var(--navy);
    color: #ffffff; font-size: 8.4px; letter-spacing: 0.2px;
    display: flex; align-items: center; justify-content: center;
  }

  .letterhead {
    position: absolute;
    left: 609px; top: 360px;
    width: 405px; height: 566px;
    background: var(--paper);
    border-top: 1px solid var(--flap);
    box-shadow: 0 1px 3px rgba(0,0,0,0.18);
  }
  .letterhead__brand {
    position: absolute; left: 58px; top: 54px;
    display: flex; align-items: center; gap: 8px;
  }
  .brand-dot {
    width: 22px; height: 22px; border-radius: 50%;
    border: 2px solid var(--brand-blue); box-sizing: border-box;
  }
  .brand-name {
    color: var(--brand-blue); font-weight: 600; font-size: 13px; letter-spacing: 0.5px;
  }
  .letterhead__company {
    position: absolute; left: 58px; top: 144px;
    font-size: 8.6px; font-weight: 600; line-height: 12px;
    color: var(--ink); margin: 0; white-space: nowrap;
  }
  .letterhead__contact {
    position: absolute; left: 59px; top: 467px;
    font-size: 7.4px; line-height: 12.5px; color: var(--ink);
    white-space: nowrap;
  }
  .letterhead__address { margin-top: 10px; font-size: 8.2px; line-height: 11.5px; }
  .letterhead__address em { font-weight: 500; }
</style>
</head>
<body>
<main class="canvas">

  <section class="envelope" aria-label="Envelope">
    <svg class="envelope__flap" width="404" height="84" viewBox="0 0 404 84">
      <path d="M2 0 H402 L396 48 Q392 76 364 78 H40 Q12 76 8 48 Z" fill="var(--flap)"/>
      <circle cx="202" cy="42" r="15" fill="none" stroke="var(--flap-mark)" stroke-width="1.6"/>
    </svg>
    <svg class="envelope__watermark" width="200" height="200" viewBox="0 0 200 200">
      <circle cx="86" cy="82" r="82" fill="none" stroke="var(--faint)" stroke-width="2"/>
      <text x="86" y="87" text-anchor="middle" font-family="Poppins, sans-serif" font-weight="600" font-size="15" fill="var(--faint)" letter-spacing="1">BORUMAND TALAJ</text>
    </svg>
    <div class="envelope__rule"></div>
    <div class="envelope__band">www.borumandtalaj-example.com</div>
  </section>

  <section class="letterhead" aria-label="Letterhead">
    <div class="letterhead__brand">
      <span class="brand-dot"></span>
      <span class="brand-name">BORUMAND TALAJ</span>
    </div>
    <p class="letterhead__company">BORUMAND TALAJ<br>INTERNATIONAL TRANSPORTATION CO</p>
    <div class="letterhead__contact">
      <div>Email: info@borumandtalaj-example.com</div>
      <div>Phone: +98 21 55402913 | Fax: +98 21 55406287</div>
      <div class="letterhead__address"><em>Address:</em> No.8, 2nd Sadaf<br>Kuy-e-Nilufari, Tehran, IRAN</div>
    </div>
  </section>

</main>
</body>
</html>
```